Meridel Capra SA Business Cards

Dear all,
Thank you for reading my brief and project. My company is doing doing advisory in real estate and to comapnies + real estates services as asset management, brokerage, development etc.
I would like to get a business card for my company which is clear, professionnal and serious.
Please have a look to the attachement to see the logos of the company

Industry/Entity Type

Real Estate

Contact Information for Business Card

I would like to have in the business card the following
Principal side:
- Logo of the company (or Monogram)
- First and Last Name (Paulo Vestrand)
- Mobile number
- email address

Second side:
- Address (Chemin des Orvets 17, 1226 Thônex - Switzerland)
- website (www.meridelcapra.ch)

Requirements
Must have
• Refer to the typeface and logo colors

```html
<!DOCTYPE html>
<html lang="en">
<head>
<meta charset="utf-8">
<title>Meridel Capra SA – Business Cards</title>
<link rel="stylesheet" href="https://fonts.googleapis.com/css2?family=Montserrat:wght@400;500;700&display=swap">
<style>
  :root {
    --backdrop: #1c1d20;
    --card-white: #ffffff;
    --card-slate: #4a5466;
    --ink-dark: #3a4250;
    --ink-muted: #5c6370;
    --accent-blue: #2b7fd0;
    --stripe-dark: #3c4452;
    --rule: #c9ced6;
  }
  * { box-sizing: border-box; margin: 0; padding: 0; }
  html, body {
    width: 900px; height: 1200px; overflow: hidden;
    background: var(--backdrop);
    font-family: "Montserrat", Arial, sans-serif;
  }
  .canvas { position: relative; width: 900px; height: 1200px; }

  .card {
    position: absolute; left: 81px; width: 732px; height: 429px;
    border-radius: 22px; overflow: hidden;
  }
  .card--front { top: 126px; background: var(--card-white); }
  .card--back  { top: 645px; background: var(--card-slate); }

  .brand {
    position: absolute; display: flex; align-items: center; gap: 16px;
  }
  .brand__square { width: 34px; height: 34px; }
  .brand__name {
    font-weight: 700; font-size: 21px; letter-spacing: 0.5px; text-transform: uppercase;
  }
  .card--front .brand { left: 96px; top: 196px; }
  .card--front .brand__square { background: var(--ink-dark); }
  .card--front .brand__name { color: var(--ink-dark); }

  .card--back .brand { left: 50%; top: 206px; transform: translateX(-50%); }
  .card--back .brand__square { background: var(--card-white); }
  .card--back .brand__name { color: var(--card-white); }

  .contact {
    position: absolute; left: 399px; top: 102px;
    border-left: 1px solid var(--rule); padding-left: 20px;
    color: var(--ink-muted); font-size: 15px; line-height: 24px;
  }
  .contact__name { font-size: 19px; letter-spacing: 0.6px; margin-bottom: 10px; text-transform: uppercase; }
  .contact__first { font-weight: 700; color: var(--ink-dark); }
  .contact__last { font-weight: 500; color: var(--accent-blue); }
  .contact__line { display: flex; align-items: center; gap: 12px; }
  .contact__line svg { width: 14px; height: 14px; flex: none; }
  .contact__address { margin-top: 16px; }

  .stripe { position: absolute; bottom: 0; height: 12px; }
  .stripe--dark { left: 0; width: 455px; background: var(--stripe-dark); }
  .stripe--blue { left: 455px; right: 0; background: var(--accent-blue); }

  .website {
    position: absolute; left: 0; right: 0; top: 378px;
    text-align: center; color: var(--card-white); font-size: 14px; letter-spacing: 0.4px;
  }
</style>
</head>
<body>
<main class="canvas">

  <section class="card card--front" aria-label="Front of card">
    <div class="brand">
      <span class="brand__square"></span>
      <span class="brand__name">Meridel Capra</span>
    </div>

    <div class="contact">
      <p class="contact__name"><span class="contact__first">Paulo</span> <span class="contact__last">Vestrand</span></p>
      <p class="contact__line">
        <svg viewBox="0 0 16 16" aria-hidden="true"><path fill="#2b7fd0" d="M3.6 1.2l2.3 2.6-1.3 1.8c.9 2 2.5 3.7 4.6 4.7l1.8-1.3 2.6 2.2-1.4 2.6C6.5 13.6 2.3 9.4 1.2 3z"/></svg>
        0227 463 051
      </p>
      <p class="contact__line">
        <svg viewBox="0 0 16 16" aria-hidden="true"><rect x="1" y="3" width="14" height="10" rx="1" fill="#2b7fd0"/><path d="M1.5 4L8 9l6.5-5" stroke="#fff" stroke-width="1.3" fill="none"/></svg>
        paulo@meridelcapra.com
      </p>
      <p class="contact__line">
        <svg viewBox="0 0 16 16" aria-hidden="true"><circle cx="8" cy="8" r="7" fill="#2b7fd0"/><path d="M1 8h14M8 1c-3 3.5-3 10.5 0 14M8 1c3 3.5 3 10.5 0 14" stroke="#fff" stroke-width="1" fill="none"/></svg>
        www.meridelcapra.ch
      </p>
      <p class="contact__address">Chemin des Orvets 17<br>1226 Thônex<br>Switzerland</p>
    </div>

    <span class="stripe stripe--dark"></span>
    <span class="stripe stripe--blue"></span>
  </section>

  <section class="card card--back" aria-label="Back of card">
    <div class="brand">
      <span class="brand__square"></span>
      <span class="brand__name">Meridel Capra</span>
    </div>
    <p class="website">www.meridelcapra.ch</p>
  </section>

</main>
</body>
</html>
```